Brenlow Development and Management Corp Stationery Design Project

Based on the logo, a stationary format that can be used for correspondence with all project stakeholders. Typically this involves landowners, public officials, general public, and investors. It needs to be clean and professional, representing the two engineers that manage the company.
Updates

Reason: Logo design finalized. Project updated for revisitation. Thanks,

Target Market(s)

Public officials, investors, project stakeholders, and landowners. All or english speaking, residing in North America. Company is based in Calgary, Alberta, Canada. Project values range fro $10MM to $500MM CAD.

Industry/Entity Type

It Company

Requirements
Should not have
• No references to tropics, palm trees, or similar beaches.

```html
<!DOCTYPE html>
<html lang="en">
<head>
<meta charset="utf-8">
<title>Brenlow Development and Management Corp — Stationery</title>
<link href="https://fonts.googleapis.com/css2?family=PT+Sans:wght@400;700&display=swap" rel="stylesheet">
<style>
  :root{
    --canvas:#eeeeee;
    --paper:#f3f3f3;
    --ink:#1f1f1f;
    --grey:#7b7d80;
    --green:#8aa82a;
    --charcoal:#2b2e31;
    --sig:#dfe4ef;
  }
  *{margin:0;padding:0;box-sizing:border-box}
  html,body{width:1200px;height:754px;overflow:hidden;background:var(--canvas);font-family:"PT Sans",sans-serif;color:var(--ink)}
  .canvas{position:relative;width:1200px;height:754px}
  .sheet{position:absolute;background:var(--paper);overflow:hidden}

  .brand{position:absolute;display:flex;flex-direction:column;align-items:flex-start}
  .brand-row{display:flex;align-items:center;gap:6px}
  .brand-mark{background:var(--green);display:block}
  .brand-name{font-family:"PT Sans",sans-serif;font-weight:700;color:var(--green);letter-spacing:.02em;line-height:1}
  .brand-tag{color:var(--grey);line-height:1.2;white-space:nowrap}
  .rule{position:absolute;left:0;height:2px;background:var(--green)}

  /* letterhead */
  .letterhead{left:100px;top:34px;width:480px;height:681px}
  .letterhead .rule{top:64px;width:272px}
  .letterhead .brand{left:286px;top:26px}
  .letterhead .brand-mark{width:14px;height:14px}
  .letterhead .brand-name{font-size:28px}
  .letterhead .brand-tag{font-size:8.5px;margin-left:20px;margin-top:2px}
  .letter{position:absolute;left:52px;top:190px;width:372px;font-size:8.2px;line-height:9.8px}
  .letter p{margin-bottom:19px}
  .letter .closing{margin-top:22px;margin-bottom:12px}
  .letter .closing strong{font-weight:700}
  .signature{position:absolute;left:52px;top:480px;width:88px;height:68px;background:var(--sig)}
  .letter-footer{position:absolute;left:25px;right:25px;top:644px;display:flex;justify-content:space-between;align-items:center;font-size:8.4px;white-space:nowrap}
  .letter-footer span{display:flex;align-items:center;gap:3px}
  .icon{width:7px;height:7px;flex:none}

  /* envelopes */
  .envelope-back{left:624px;top:34px;width:539px;height:259px}
  .flap{position:absolute;left:0;top:0;width:539px;height:92px;background:var(--charcoal);border-radius:0 0 10px 10px}
  .flap .brand{left:206px;top:34px}
  .flap .brand-mark{width:10px;height:10px}
  .flap .brand-name{font-size:17px}
  .flap .brand-tag{font-size:5.3px;margin-left:16px;margin-top:2px}

  .envelope-front{left:624px;top:314px;width:539px;height:258px}
  .envelope-front .rule{top:73px;width:312px}
  .envelope-front .brand{left:326px;top:30px}
  .envelope-front .brand-mark{width:14px;height:14px}
  .envelope-front .brand-name{font-size:31px}
  .envelope-front .brand-tag{font-size:9px;margin-left:20px;margin-top:2px}
  .return-address{position:absolute;right:32px;top:216px;font-size:7.2px}

  /* business cards */
  .card-front{left:624px;top:593px;width:218px;height:123px}
  .card-front .rule{top:37px;width:106px;height:1.5px}
  .card-front .brand{left:110px;top:16px}
  .card-front .brand-mark{width:7px;height:7px}
  .card-front .brand-name{font-size:15px}
  .card-front .brand-tag{font-size:3.8px;margin-left:13px;margin-top:1px}
  .card-address{position:absolute;left:11px;top:63px;font-size:5px;line-height:6px}
  .card-contacts{position:absolute;left:11px;top:81px;list-style:none;font-size:4.8px;line-height:7.6px}
  .card-contacts li{display:flex;align-items:center;gap:3px}
  .card-contacts .icon{width:4px;height:4px}
  .card-person{position:absolute;right:12px;top:63px;text-align:right;font-size:5px;line-height:6px}
  .card-person .name{color:var(--green)}

  .card-back{left:866px;top:593px;width:219px;height:123px;background:var(--charcoal)}
  .card-back .brand{left:16px;top:22px}
  .card-back .brand-mark{width:7px;height:7px}
  .card-back .brand-name{font-size:15px}
  .card-back .brand-tag{font-size:3.8px;margin-left:13px;margin-top:1px}
</style>
</head>
<body>
<main class="canvas">

  <!-- Letterhead -->
  <section class="sheet letterhead" aria-label="Letterhead">
    <div class="rule"></div>
    <div class="brand">
      <div class="brand-row"><span class="brand-mark"></span><span class="brand-name">BRENLOW</span></div>
      <span class="brand-tag">Development and Management Corp</span>
    </div>

    <div class="letter">
      <p>Dear Mr. Arthur Bell</p>
      <p>Lorem ipsum dolor sit amet, consectetuer adipiscing elit. Aenean commodo ligula eget dolor. Aenean massa. Cum sociis natoque penatibus et magnis dis parturient montes, nascetur ridiculus mus. Donec quam felis, ultricies nec, pellentesque eu, pretium quis, sem. Nulla consequat massa quis enim. Donec pede justo, fringilla vel, aliquet nec, vulputate eget, arcu.</p>
      <p>In enim justo, rhoncus ut, imperdiet a, venenatis vitae, justo. Nullam dictum felis eu pede mollis pretium. Integer tincidunt. Cras dapibus. Vivamus elementum semper nisi. Aenean vulputate eleifend tellus. Aenean leo ligula, porttitor eu, consequat vitae, eleifend ac, enim. Aliquam lorem ante, dapibus in, viverra quis, feugiat a, tellus.</p>
      <p>Phasellus viverra nulla ut metus varius laoreet. Quisque rutrum. Aenean imperdiet. Etiam ultricies nisi vel augue. Curabitur ullamcorper ultricies nisi. Nam eget dui. Etiam rhoncus. Maecenas tempus, tellus eget condimentum rhoncus, sem quam semper libero, sit amet adipiscing sem neque sed ipsum. Nam quam nunc, blandit vel, luctus pulvinar, hendrerit id, lorem. Maecenas nec odio et ante tincidunt tempus. Donec vitae sapien ut libero venenatis faucibus. Nullam quis ante. Etiam sit amet orci eget eros faucibus tincidunt. Duis leo. Sed fringilla mauris sit amet nibh. Donec sodales sagittis magna. Sed consequat, leo eget bibendum sodales, augue velit cursus nunc,</p>
      <p class="closing"><strong>Sincerely,</strong><br>Morgan<br>General Manager</p>
    </div>
    <div class="signature" role="img" aria-label="Handwritten signature of the general manager"></div>

    <footer class="letter-footer">
      <span>418 Marlowe Street, Calgary, AB T2P 1K4</span>
      <span><svg class="icon" viewBox="0 0 10 10"><path d="M2 1h2l1 2.5-1.3 1a5 5 0 0 0 2.8 2.8l1-1.3L10 7v2a1 1 0 0 1-1 1A9 9 0 0 1 0 1a1 1 0 0 1 1-1z" fill="var(--green)"/></svg>403-555-0142</span>
      <span><svg class="icon" viewBox="0 0 10 10"><rect x="1" y="3" width="8" height="6" rx="1" fill="var(--green)"/><rect x="3" y="1" width="4" height="2" fill="var(--green)"/></svg>403-555-0143</span>
      <span><svg class="icon" viewBox="0 0 10 10"><circle cx="5" cy="5" r="4" fill="none" stroke="var(--green)" stroke-width="1.5"/><circle cx="5" cy="5" r="1.5" fill="var(--green)"/></svg>info@brenlow.com</span>
      <span><svg class="icon" viewBox="0 0 10 10"><circle cx="5" cy="5" r="4.3" fill="none" stroke="var(--green)" stroke-width="1.2"/><path d="M1 5h8M5 1c-2 2.5-2 5.5 0 8M5 1c2 2.5 2 5.5 0 8" fill="none" stroke="var(--green)" stroke-width=".8"/></svg>www.brenlow.com</span>
    </footer>
  </section>

  <!-- Envelope, flap side -->
  <section class="sheet envelope-back" aria-label="Envelope back">
    <div class="flap">
      <div class="brand">
        <div class="brand-row"><span class="brand-mark"></span><span class="brand-name">BRENLOW</span></div>
        <span class="brand-tag">Development and Management Corp</span>
      </div>
    </div>
  </section>

  <!-- Envelope, address side -->
  <section class="sheet envelope-front" aria-label="Envelope front">
    <div class="rule"></div>
    <div class="brand">
      <div class="brand-row"><span class="brand-mark"></span><span class="brand-name">BRENLOW</span></div>
      <span class="brand-tag">Development and Management Corp</span>
    </div>
    <p class="return-address">418 Marlowe Street, Calgary, AB T2P 1K4</p>
  </section>

  <!-- Business card, front -->
  <section class="sheet card-front" aria-label="Business card front">
    <div class="rule"></div>
    <div class="brand">
      <div class="brand-row"><span class="brand-mark"></span><span class="brand-name">BRENLOW</span></div>
      <span class="brand-tag">Development and Management Corp</span>
    </div>
    <p class="card-address">418 Marlowe Street<br>Calgary, AB T2P 1K4</p>
    <ul class="card-contacts">
      <li><svg class="icon" viewBox="0 0 10 10"><circle cx="5" cy="5" r="5" fill="var(--green)"/></svg>403-555-0142</li>
      <li><svg class="icon" viewBox="0 0 10 10"><circle cx="5" cy="5" r="5" fill="var(--green)"/></svg>403-555-0143</li>
      <li><svg class="icon" viewBox="0 0 10 10"><circle cx="5" cy="5" r="5" fill="var(--green)"/></svg>dana@brenlow.com</li>
      <li><svg class="icon" viewBox="0 0 10 10"><circle cx="5" cy="5" r="5" fill="var(--green)"/></svg>www.brenlow.com</li>
    </ul>
    <p class="card-person"><span class="name">Dana Whitfield</span><br>Director</p>
  </section>

  <!-- Business card, back -->
  <section class="sheet card-back" aria-label="Business card back">
    <div class="brand">
      <div class="brand-row"><span class="brand-mark"></span><span class="brand-name">BRENLOW</span></div>
      <span class="brand-tag">Development and Management Corp</span>
    </div>
  </section>

</main>
</body>
</html>
```